Webdesign für Unternehmensberatung
Zielgruppe
Die kvr Consulting GmbH (kurz KVR) ist eine 2014 gegründete Unternehmensberatung, deren Haupttätigkeit die Beratung ausländischer Unternehmen zum Thema Markteintritt in Deutschland ist. Die Unternehmens-Website ist ein wesentliches Instrument, durch das KVR sein Beratungsangebot an potentielle Kunden im Ausland kommuniziert.
Die Zielgruppe sind ausländische Unternehmen, die planen einen Markteintritt in Deutschland zu realisieren.
Aufgabenstellung
Insgesamt soll die Seite Stärke, Professionalität und Modernität ausstrahlen.
Ziele des neuen Designs
• Das neue Design soll die Professionalität des Unternehmens unterstützen und im besten Fall beim Besucher einen kleinen „Wow-Effekt“ auslösen
• Wichtig! Die Zielgruppen sind ausländische Unternehmen aus Ländern wie Indien, Spanien, Dänemark, Finnland, Ungarn, USA usw. D. h. dass das ganze gern „flashy“ sein darf, typisch deutsches „Understatement“ ist hier nicht gefragt.
• Das Design muss die Funktion enthalten, die Sprachen zu wechseln.
• Ein Standarddesign, welches von jedem Templateshop übernommen werden
kann, ist nicht erwünscht.
• Das Design soll ausgerichtet sein für Seiten, die vorrangig Text enthalten, dann
für Seiten mit Bildern im Text, sowie primäre Bild-Seiten sowie Seiten für eine Grafiksprache zu verstehen als Dashboard, mit entsprechenden Animationen oder Icons.
• Adaptionen des Logos sind möglich, jedoch ist das Logo als Ganzes (kv Streifen + Schriftzug) zu verwenden.
• Verwenden Sie bitte ausschließlich Icons, die nicht überall zu finden sind
• Bitte fügen Sie die Menüstruktur hinzu, die in dem Anforderungsdokument ganz unten zu finden sind

```html
<!DOCTYPE html>
<html lang="en">
<head>
<meta charset="utf-8">
<title>kvr Consulting – Market Entry Germany</title>
<link href="https://fonts.googleapis.com/css2?family=Poppins:wght@300;400;500;600&display=swap" rel="stylesheet">
<style>
  :root {
    --page-bg: #ececec;
    --white: #ffffff;
    --ink: #111111;
    --muted: #b9b9b9;
    --yellow: #ffcc00;
    --stage-top: #eef2f3;
    --stage-bottom: #e3e9eb;
    --art-a: #cfe3ea;
    --art-b: #f2d7a8;
  }
  * { margin: 0; padding: 0; box-sizing: border-box; }
  html, body { width: 1200px; height: 1161px; overflow: hidden; }
  body {
    background: var(--page-bg);
    font-family: "Poppins", sans-serif;
    font-weight: 300;
    color: var(--ink);
    position: relative;
  }
  .site {
    position: absolute; left: 0; top: 241px;
    width: 1200px; height: 679px;
    background: var(--white);
    overflow: hidden;
  }
  /* left column */
  .sidebar { position: absolute; left: 0; top: 0; width: 260px; height: 100%; background: var(--white); }
  .lang-switch { position: absolute; left: 15px; top: 29px; display: flex; align-items: center; gap: 8px; }
  .brand { position: absolute; left: 15px; top: 228px; display: flex; align-items: center; gap: 8px; }
  .brand-square { width: 22px; height: 22px; background: var(--ink); }
  .brand-name { font-size: 26px; font-weight: 400; letter-spacing: -1px; line-height: 1; color: var(--ink); }
  .brand-sub { position: absolute; left: 15px; top: 262px; font-size: 12px; font-weight: 400; line-height: 1.05; color: var(--ink); }
  .main-nav { position: absolute; left: 15px; top: 360px; width: 210px; list-style: none; }
  .main-nav li {
    display: flex; justify-content: space-between; align-items: center;
    height: 22.4px; font-size: 11px; letter-spacing: -0.5px; color: var(--muted); text-transform: uppercase;
  }
  .main-nav li.is-active { color: var(--ink); font-weight: 400; text-decoration: underline; }
  .copyright { position: absolute; left: 15px; top: 649px; font-size: 10px; letter-spacing: -0.4px; }

  /* center stage */
  .stage {
    position: absolute; left: 260px; top: 0; width: 612px; height: 100%;
    background: linear-gradient(160deg, var(--stage-top) 0%, #f7f9f9 45%, var(--stage-bottom) 100%);
  }
  .stage-title { position: absolute; left: 58px; top: 40px; line-height: 1; letter-spacing: -1.2px; }
  .stage-title .lead { display: block; font-size: 25px; }
  .stage-title .big { display: block; font-size: 41px; margin-top: -4px; letter-spacing: -2px; }
  .stage-art {
    position: absolute; left: 222px; top: 166px; width: 150px; height: 133px; border-radius: 6px;
    background: radial-gradient(circle at 50% 45%, var(--art-a) 0%, var(--art-b) 55%, rgba(242,215,168,0) 75%);
  }
  .slider-dots { position: absolute; left: 65px; top: 333px; display: flex; gap: 6px; }
  .slider-dots i { width: 3px; height: 3px; border-radius: 50%; background: var(--muted); display: block; }
  .slider-dots i.on { background: #555; width: 4px; height: 4px; }
  .slide-title { position: absolute; left: 65px; top: 350px; font-size: 25px; font-weight: 600; letter-spacing: -1.5px; color: var(--yellow); }
  .slide-text { position: absolute; left: 65px; top: 392px; width: 475px; font-size: 15px; line-height: 16.4px; letter-spacing: -0.8px; }
  .btn-more {
    position: absolute; left: 250px; top: 485px; width: 106px; height: 32px;
    background: var(--white); font-size: 13px; font-weight: 400; letter-spacing: -0.8px;
    display: flex; align-items: center; justify-content: center;
    box-shadow: 0 2px 6px rgba(0,0,0,0.06);
  }
  .news-card {
    position: absolute; left: 60px; top: 553px; width: 492px; height: 97px;
    background: var(--yellow); color: var(--white); padding: 12px 14px;
  }
  .news-label { font-size: 10px; text-transform: uppercase; letter-spacing: -0.4px; }
  .news-dots { position: absolute; right: 20px; top: 18px; display: flex; gap: 5px; }
  .news-dots i { width: 3px; height: 3px; border-radius: 50%; background: rgba(255,255,255,0.6); display: block; }
  .news-dots i.on { background: var(--white); width: 4px; height: 4px; }
  .news-headline { margin-top: 9px; font-size: 21px; font-weight: 500; line-height: 22px; letter-spacing: -1.4px; }
  .news-date { font-size: 11px; font-weight: 300; letter-spacing: -0.6px; }

  /* right column */
  .intro { position: absolute; left: 872px; top: 0; width: 328px; height: 100%; text-align: right; }
  .intro-heading { position: absolute; right: 10px; top: 35px; width: 300px; font-size: 19px; font-weight: 500; line-height: 20px; letter-spacing: -1.2px; color: var(--yellow); }
  .intro-text { position: absolute; right: 15px; width: 300px; font-size: 14.5px; line-height: 14.5px; letter-spacing: -0.9px; }
  .intro-text.first { top: 107px; }
  .intro-text.second { top: 252px; }
  .intro-text strong { font-weight: 500; }
  .intro-cta { position: absolute; right: 10px; top: 441px; width: 300px; font-size: 15px; font-weight: 500; line-height: 15px; letter-spacing: -0.9px; }
  .footer-links { position: absolute; right: 15px; top: 582px; padding-right: 15px; border-right: 1px solid #e2e2e2; list-style: none; }
  .footer-links li { font-size: 11px; letter-spacing: -0.5px; color: var(--muted); height: 23px; line-height: 23px; text-transform: uppercase; }
</style>
</head>
<body>
<main class="site">
  <aside class="sidebar">
    <div class="lang-switch" aria-label="Language: English">
      <svg width="20" height="12" viewBox="0 0 20 12">
        <rect width="20" height="12" fill="#c8102e"/>
        <rect y="1.7" width="20" height="1.7" fill="#fff"/>
        <rect y="5.1" width="20" height="1.7" fill="#fff"/>
        <rect y="8.5" width="20" height="1.7" fill="#fff"/>
        <rect width="9" height="6.8" fill="#1f3a93"/>
      </svg>
      <svg width="9" height="6" viewBox="0 0 9 6"><path d="M1 1l3.5 3.5L8 1" fill="none" stroke="#bbb" stroke-width="1"/></svg>
    </div>
    <div class="brand">
      <span class="brand-square"></span>
      <span class="brand-name">kv</span>
    </div>
    <div class="brand-sub">kvr<br>consulting<br>germany</div>
    <ul class="main-nav">
      <li class="is-active">About us <svg width="9" height="6" viewBox="0 0 9 6"><path d="M1 1l3.5 3.5L8 1" fill="none" stroke="#ffcc00" stroke-width="1.4"/></svg></li>
      <li>Services <svg width="9" height="6" viewBox="0 0 9 6"><path d="M1 1l3.5 3.5L8 1" fill="none" stroke="#ccc" stroke-width="1"/></svg></li>
      <li>About Germany <svg width="9" height="6" viewBox="0 0 9 6"><path d="M1 1l3.5 3.5L8 1" fill="none" stroke="#ccc" stroke-width="1"/></svg></li>
      <li>Dashboard <svg width="9" height="6" viewBox="0 0 9 6"><path d="M1 1l3.5 3.5L8 1" fill="none" stroke="#ccc" stroke-width="1"/></svg></li>
      <li>Clients <svg width="9" height="6" viewBox="0 0 9 6"><path d="M1 1l3.5 3.5L8 1" fill="none" stroke="#ccc" stroke-width="1"/></svg></li>
      <li>News <svg width="9" height="6" viewBox="0 0 9 6"><path d="M1 1l3.5 3.5L8 1" fill="none" stroke="#ccc" stroke-width="1"/></svg></li>
    </ul>
    <p class="copyright">© kvr 2018</p>
  </aside>

  <section class="stage" role="img" aria-label="Pale background photo of a modern glass office building">
    <h1 class="stage-title"><span class="lead">Your main point of contact for the</span><span class="big">German market.</span></h1>
    <div class="stage-art" role="img" aria-label="Illustration of a laptop with charts and a magnifying glass"></div>
    <div class="slider-dots"><i></i><i></i><i></i><i class="on"></i><i></i><i></i><i></i></div>
    <h2 class="slide-title">MARKET ENTRY</h2>
    <p class="slide-text">Swift, efficient and cost-effective entry into the German market. After undertaking an initial comprehensive evaluation of your project, we develop purposeful steps for the optimal placement of your product on the German market.</p>
    <div class="btn-more">Learn More...</div>
    <article class="news-card">
      <div class="news-label">News</div>
      <div class="news-dots"><i></i><i></i><i></i><i class="on"></i><i></i><i></i><i></i></div>
      <p class="news-headline">KVR becomes member of the Nordic-German<br>Trade Circle NRW <span class="news-date">16 december 2018</span></p>
    </article>
  </section>

  <section class="intro">
    <h2 class="intro-heading">Are you looking for a successful launch on the German market?</h2>
    <p class="intro-text first">We support companies with their market entry into Europe's key market with a dedicated team who are experts in their respective fields. By working with us, you will have instant access to all the necessary know-how and expertise that is necessary to succeed in this attractive but demanding market.</p>
    <p class="intro-text second">Our core focus is on sales and marketing success of our clients and our approach is proven, pragmatic and success-oriented. With us, you have a single point of contact for the German market, and we will coordinate all relevant measures and services on your behalf. Our team looks forward to working with and for you: call us today at <strong>+49 (0) 221 12 34 56 78</strong> or write an <strong>email</strong>.</p>
    <p class="intro-cta">Want to launch your company on the German market? We show you how!</p>
    <ul class="footer-links">
      <li>Contact us</li>
      <li>Imprint</li>
      <li>Packages</li>
    </ul>
  </section>
</main>
</body>
</html>
```